letterhead design for a investing company*

Design an appealing business letterhead to match with our existing logo and attract new customers. Our customers are mainly corporate managers which are detail oriented and judge the company ability to perform a good service based on small details. A professional letterhead will give a good first impression.

Target Market(s)

New customers and business owners

Industry/Entity Type

Marketplace

Font styles to use
Sans Serif
Script

Requirements
Must have
• Must be a professional and elegant design that attracts interest from people who receives it

```html
<!DOCTYPE html>
<html lang="en">
<head>
<meta charset="utf-8">
<title>Norvane Letterhead</title>
<link href="https://fonts.googleapis.com/css2?family=Encode+Sans+Semi+Condensed:wght@300;400;600&family=Lato:wght@400&display=swap" rel="stylesheet">
<style>
  :root {
    --navy: #121c3c;
    --gold: #fbb913;
    --ink: #555a60;
    --muted: #6a6e73;
    --stage: #d6d6d6;
    --paper: #ffffff;
  }
  html, body {
    margin: 0;
    padding: 0;
    width: 1056px;
    height: 1200px;
    overflow: hidden;
    background: var(--stage);
  }
  .letterhead {
    position: absolute;
    left: 104px;
    top: 0;
    width: 848px;
    height: 1200px;
    background: var(--paper);
    font-family: "Encode Sans Semi Condensed", sans-serif;
    color: var(--ink);
  }
  .brand {
    position: absolute;
    top: 92px;
    left: 0;
    width: 848px;
    display: flex;
    justify-content: center;
    align-items: center;
    gap: 14px;
  }
  .brand-dot {
    width: 44px;
    height: 44px;
    border-radius: 50%;
    background: var(--gold);
  }
  .brand-name {
    font-family: "Encode Sans Semi Condensed", sans-serif;
    font-weight: 600;
    font-size: 64px;
    line-height: 1;
    color: var(--navy);
    letter-spacing: 0.5px;
  }
  .letter-body {
    position: absolute;
    left: 79px;
    top: 342px;
    width: 688px;
    font-weight: 300;
    font-size: 17.5px;
    line-height: 29.5px;
  }
  .letter-body p {
    margin: 0 0 29px 0;
    text-align: justify;
  }
  .salutation { margin-bottom: 26px !important; }
  .closing {
    position: absolute;
    left: 79px;
    top: 944px;
    font-weight: 300;
    font-size: 17.5px;
    margin: 0;
  }
  .signature {
    position: absolute;
    left: 77px;
    top: 978px;
    width: 70px;
    height: 44px;
    background: linear-gradient(135deg, #fde3a0, #fcd06a);
    border-radius: 4px;
  }
  .contact-bar {
    position: absolute;
    left: 79px;
    top: 1114px;
    width: 688px;
    height: 34px;
    font-family: "Lato", sans-serif;
    font-size: 13.5px;
    line-height: 17px;
    color: var(--muted);
  }
  .contact-col { position: absolute; top: 0; }
  .contact-address { left: 0; }
  .contact-phone { left: 294px; }
  .contact-web { right: 0; }
  .contact-line { display: flex; align-items: center; gap: 8px; white-space: nowrap; }
  .contact-line svg { width: 10px; height: 10px; flex: none; }
  .divider {
    position: absolute;
    top: 5px;
    width: 1.5px;
    height: 25px;
    background: var(--gold);
  }
  .divider-one { left: 229px; }
  .divider-two { left: 472px; }
  .footer-band {
    position: absolute;
    left: 0;
    bottom: 7px;
    width: 848px;
    height: 21px;
  }
</style>
</head>
<body>
  <main class="letterhead">
    <header class="brand">
      <span class="brand-dot"></span>
      <span class="brand-name">Norvane</span>
    </header>

    <section class="letter-body">
      <p class="salutation">Dear Sir/Mam,</p>
      <p>Contrary to popular belief, Lorem Ipsum is not simply random text. It has roots in a piece of classical Latin literature from 45 BC, making it over 2000 years old. Daniel Mercer, a Latin professor at Ashford College in Westmere, looked up one of the more obscure Latin words, consectetur.</p>
      <p>Lorem Ipsum comes from sections 1.10.32 and 1.10.33 of "de Finibus Bonorum et Malorum" (The Extremes of Good and Evil) by Tullian, written in 45 BC. This book is a treatise on the theory of ethics, very popular during the Renaissance. The first line of Lorem Ipsum.</p>
      <p>The standard chunk of Lorem Ipsum used since the 1500s is reproduced below for those interested. Sections 1.10.32 and 1.10.33 from "de Finibus Bonorum et Malorum" by Tullian are also reproduced in their exact original.</p>
      <p>The standard chunk of Lorem Ipsum used since the 1500s is reproduced below for those interested.</p>
    </section>

    <p class="closing">Best Regards</p>
    <div class="signature" role="img" aria-label="Handwritten signature of the sender"></div>

    <footer class="contact-bar">
      <div class="contact-col contact-address">
        <div class="contact-line">1234 First Line Address</div>
        <div class="contact-line">5678 Second Line Address</div>
      </div>
      <span class="divider divider-one"></span>
      <div class="contact-col contact-phone">
        <div class="contact-line">
          <svg viewBox="0 0 10 10" aria-hidden="true"><path d="M2 1 L4 3 L3 4 Q4.5 6 6 7 L7 6 L9 8 L8 9.3 Q3 9 0.7 2 Z" fill="var(--gold)"/></svg>
          444-555-7777
        </div>
        <div class="contact-line">
          <svg viewBox="0 0 10 10" aria-hidden="true"><rect x="2.5" y="0.5" width="5" height="3" fill="var(--gold)"/><rect x="0.5" y="3.5" width="9" height="4" rx="1" fill="var(--gold)"/><rect x="2.5" y="6.5" width="5" height="3" fill="var(--gold)"/></svg>
          444-555-9999
        </div>
      </div>
      <span class="divider divider-two"></span>
      <div class="contact-col contact-web">
        <div class="contact-line">
          <svg viewBox="0 0 10 10" aria-hidden="true"><rect x="0.5" y="1.5" width="9" height="7" fill="var(--gold)"/><path d="M0.5 1.5 L5 5.5 L9.5 1.5" stroke="#fff" stroke-width="1" fill="none"/></svg>
          contact@yourmail.com
        </div>
        <div class="contact-line">
          <svg viewBox="0 0 10 10" aria-hidden="true"><circle cx="5" cy="5" r="4.5" fill="var(--gold)"/><ellipse cx="5" cy="5" rx="2" ry="4.5" stroke="#fff" stroke-width="0.7" fill="none"/><line x1="0.5" y1="5" x2="9.5" y2="5" stroke="#fff" stroke-width="0.7"/></svg>
          www.yourwebsite.com
        </div>
      </div>
    </footer>

    <svg class="footer-band" viewBox="0 0 848 21" preserveAspectRatio="none" aria-hidden="true">
      <polygon points="0,0 617,0 596,21 0,21" fill="var(--navy)"/>
      <polygon points="627,0 848,0 848,21 606,21" fill="var(--gold)"/>
    </svg>
  </main>
</body>
</html>
```